RT Advisory - Web Design Upgrade

We have recently designed a website (http://www.rtadvisory-example.com.au) which requires more creative and professional inputs. The website was designed using 'bright hosting site builder template' and it is currently available for viewing on the internet. Also, you are able to access the PDF files for the 6 main pages (i.e. Home, About, Services, Contaminated Land Management, Groundwater Management and Contact).

The current website has 17 pages, however, your design may only be required for the 6 main pages.

Currently the website background is white but we are open to other colours provided the company logo is adjusted accordingly.

The idea is to upgrade the existing design and, if possible, continue using 'bright hosting' as the preferred web host. So we are not sure if the design should be coded or uncoded...we leave it to your proficiency and advice.

Target Market(s)

Government organisations, landowners and developers, waste and utilities companies, community organisations and individuals.

Font styles to use
Sans Serif

Colors
0355a3
3176b5
9ccb3b
acd037
ffffff

Requirements
Nice to have
• Sliding images

```html
<!DOCTYPE html>
<html lang="en">
<head>
<meta charset="utf-8">
<title>RT Advisory – Home</title>
<link rel="stylesheet" href="https://fonts.googleapis.com/css2?family=Ubuntu:ital,wght@0,400;0,500;0,700;1,500&family=Open+Sans:wght@400&family=PT+Sans&display=swap">
<style>
:root{
  --brand-blue:#34399a;
  --brand-blue-dark:#2b3190;
  --olive:#5b6b1f;
  --olive-light:#8c9a62;
  --leaf:#6f7f23;
  --grey-text:#777;
  --body-text:#555;
  --rule:#c8c8c8;
  --white:#fff;
}
*{box-sizing:border-box;margin:0;padding:0}
html,body{width:988px;height:1200px;overflow:hidden;background:var(--white)}
body{position:relative;font-family:"Ubuntu",sans-serif;color:#333}
.abs{position:absolute}

.brand{left:18px;top:44px;display:flex;align-items:center;gap:10px}
.brand-dot{width:40px;height:40px;border-radius:50%;background:var(--brand-blue)}
.brand-name{font-family:"Ubuntu",sans-serif;font-weight:500;font-size:26px;color:var(--brand-blue)}

.phone{right:43px;top:28px;font-weight:700;font-size:23px;color:var(--brand-blue);display:flex;align-items:center;gap:6px}
.address{right:43px;top:62px;font-size:16px;color:#888;display:flex;align-items:center;gap:5px;letter-spacing:.3px}

.main-nav{left:429px;top:104px;display:flex;gap:0}
.main-nav a{position:absolute;font-size:14.5px;color:#555;text-decoration:none;white-space:nowrap}
.main-nav a.active{border-bottom:2px solid var(--brand-blue);padding-bottom:1px}
.search{left:699px;top:102px;width:246px;height:26px;border:1px solid #bbb;font-family:"Open Sans",sans-serif;font-size:10.5px;color:#999;padding:6px 7px}
.search svg{position:absolute;right:6px;top:5px}

.hero{left:0;top:146px;width:988px;height:442px;
  background:linear-gradient(180deg,#3b3d42 0%,#6a6a6c 25%,#c9b58a 38%,#3f4a2c 45%,#7e94b8 60%,#5b6f98 80%,#4a5674 100%)}
.hero-sun{left:0;top:146px;width:988px;height:442px;background:radial-gradient(circle at 86% 32%,rgba(255,214,120,.85) 0,rgba(255,190,90,.35) 10%,transparent 28%)}
.slide-title{left:104px;top:322px;width:462px;height:41px;background:rgba(255,255,255,.92);clip-path:polygon(0 0,100% 0,96% 100%,0 100%);
  font-weight:500;font-style:italic;font-size:24px;color:var(--leaf);padding:6px 12px}
.slide-sub{left:104px;top:364px;width:257px;height:41px;background:var(--brand-blue);clip-path:polygon(0 0,100% 0,94% 100%,0 100%);
  font-weight:500;font-style:italic;font-size:20px;color:var(--white);padding:8px 13px}
.arrow{top:345px}

.section-title{font-weight:500;font-size:18px;color:var(--brand-blue)}
.divider{left:480px;top:610px;width:2px;height:361px;background:#ccc}
.photo-frame{width:360px;height:125px;border:1px solid var(--rule);padding:8px}
.photo{width:100%;height:100%}
.photo-leaf{background:linear-gradient(160deg,#1d3a06 0%,#5c9a14 40%,#a6d84a 60%,#4c7d10 80%,#0c1a03 100%)}
.photo-drill{background:linear-gradient(90deg,#a89e8c 0%,#c9b48a 35%,#d7b937 65%,#7b7568 100%)}

.service-list{left:87px;top:797px;list-style:none}
.service-list li{display:flex;align-items:center;gap:9px;height:23.8px;font-family:"Open Sans",sans-serif;font-size:11.2px;color:#555}
.service-list li span{text-decoration:underline}

.intro{left:537px;top:797px;width:377px;font-family:"Open Sans",sans-serif;font-size:10.7px;line-height:15px;color:var(--body-text)}
.btn-more{left:539px;top:917px;width:115px;height:31px;background:var(--brand-blue);color:var(--white);border-radius:2px;font-weight:500;font-size:12px;display:flex;align-items:center;justify-content:center}

.tagline{left:55px;top:1028px;font-family:"PT Sans",sans-serif;font-size:22.5px;line-height:28px;color:#222}

.footer{left:0;top:1115px;width:988px;height:85px;background:var(--olive)}
.legal{left:22px;top:1136px;font-size:12px;line-height:14px;color:var(--white)}
.footer-nav a{position:absolute;top:1145px;height:27px;background:var(--olive-light);color:var(--white);font-size:13px;display:flex;align-items:center;justify-content:center;text-decoration:none}
</style>
</head>
<body>

<header>
  <div class="abs brand"><span class="brand-dot"></span><span class="brand-name">RT Advisory</span></div>
  <div class="abs phone">
    <svg width="22" height="16" viewBox="0 0 22 16"><path d="M2 6c0-3 4-5 9-5s9 2 9 5l-1 2-4-1V5c-2-.7-6-.7-8 0v2L3 8z" fill="#333"/><path d="M6 9h10l3 6H3z" fill="#333"/></svg>
    +61 (0)2 9000 4127
  </div>
  <div class="abs address">
    <svg width="13" height="18" viewBox="0 0 13 18"><path d="M6.5 0C3 0 0 2.8 0 6.3 0 11 6.5 18 6.5 18S13 11 13 6.3C13 2.8 10 0 6.5 0z" fill="#555"/><circle cx="6.5" cy="6.3" r="2.4" fill="#fff"/></svg>
    48A Harbourside Lane, Marrickvale, NSW 2031
  </div>
  <nav class="main-nav">
    <a class="active" style="left:0">Home</a>
    <a style="left:62px">About</a>
    <a style="left:126px">Services</a>
    <a style="left:206px">Contact</a>
  </nav>
  <div class="abs search">Search
    <svg width="15" height="15" viewBox="0 0 15 15"><circle cx="6" cy="6" r="4.5" fill="none" stroke="#666" stroke-width="2"/><path d="M9.5 9.5 14 14" stroke="#666" stroke-width="2.4"/></svg>
  </div>
</header>

<section>
  <div class="abs hero" role="img" aria-label="Slide photo: wetland with grasses reflecting a cloudy sunset sky"></div>
  <div class="abs hero-sun"></div>
  <div class="abs slide-title">Working to Sustain our Environments</div>
  <div class="abs slide-sub">Strategic Advice</div>
  <svg class="abs arrow" style="left:12px" width="20" height="46" viewBox="0 0 20 46"><path d="M17 2 3 23l14 21" fill="none" stroke="#fff" stroke-width="2.5"/></svg>
  <svg class="abs arrow" style="left:954px" width="20" height="46" viewBox="0 0 20 46"><path d="M3 2l14 21L3 44" fill="none" stroke="#fff" stroke-width="2.5"/></svg>
</section>

<main>
  <h2 class="abs section-title" style="left:87px;top:614px">Contaminated Land Management</h2>
  <div class="abs photo-frame" style="left:77px;top:654px"><div class="photo photo-leaf" role="img" aria-label="Photo: close-up of a green leaf with water droplets"></div></div>
  <ul class="abs service-list">
    <li><svg width="17" height="15" viewBox="0 0 17 15"><rect x="1" y="2" width="12" height="12" rx="3" fill="none" stroke="#555" stroke-width="1.6"/><path d="M4 7l3 3 8-9" fill="none" stroke="#555" stroke-width="2"/></svg><span>Strategic Advice</span></li>
    <li><svg width="17" height="15" viewBox="0 0 17 15"><rect x="1" y="2" width="12" height="12" rx="3" fill="none" stroke="#555" stroke-width="1.6"/><path d="M4 7l3 3 8-9" fill="none" stroke="#555" stroke-width="2"/></svg><span>Project Management</span></li>
    <li><svg width="17" height="15" viewBox="0 0 17 15"><rect x="1" y="2" width="12" height="12" rx="3" fill="none" stroke="#555" stroke-width="1.6"/><path d="M4 7l3 3 8-9" fill="none" stroke="#555" stroke-width="2"/></svg><span>Purchase/Sale Contamination Appraisal</span></li>
    <li><svg width="17" height="15" viewBox="0 0 17 15"><rect x="1" y="2" width="12" height="12" rx="3" fill="none" stroke="#555" stroke-width="1.6"/><path d="M4 7l3 3 8-9" fill="none" stroke="#555" stroke-width="2"/></svg><span>Environmental Site Assessment</span></li>
    <li><svg width="17" height="15" viewBox="0 0 17 15"><rect x="1" y="2" width="12" height="12" rx="3" fill="none" stroke="#555" stroke-width="1.6"/><path d="M4 7l3 3 8-9" fill="none" stroke="#555" stroke-width="2"/></svg><span>Site Remediation &amp; Validation</span></li>
    <li><svg width="17" height="15" viewBox="0 0 17 15"><rect x="1" y="2" width="12" height="12" rx="3" fill="none" stroke="#555" stroke-width="1.6"/><path d="M4 7l3 3 8-9" fill="none" stroke="#555" stroke-width="2"/></svg><span>Acid Sulfate Soil Assessment &amp; Management</span></li>
    <li><svg width="17" height="15" viewBox="0 0 17 15"><rect x="1" y="2" width="12" height="12" rx="3" fill="none" stroke="#555" stroke-width="1.6"/><path d="M4 7l3 3 8-9" fill="none" stroke="#555" stroke-width="2"/></svg><span>Waste Classification &amp; Management</span></li>
  </ul>

  <div class="abs divider"></div>

  <h2 class="abs section-title" style="left:535px;top:614px">Groundwater Impact Assessment</h2>
  <div class="abs photo-frame" style="left:526px;top:654px"><div class="photo photo-drill" role="img" aria-label="Photo: drilling rig and crew working on a groundwater bore site"></div></div>
  <p class="abs intro">The potential impacts of proposed developments on groundwater are diverse and the impact of ground- water usage schemes is assessed against potential impacts on adjacent aquifers, neighbouring users and environmental receptors. Environmental receptors can include both springs and connected surface waters as well as local stygofauna. Impact assessments feed into environmental impact studies.</p>
  <div class="abs btn-more">Read More</div>

  <p class="abs tagline">We are committed to delivering innovative and cost effective<br>solutions that can achieve sustainable and reliable outcomes</p>
</main>

<footer>
  <div class="abs footer"></div>
  <p class="abs legal">Copyright © 2014 - Rural &amp; Terrain Advisory Pty Ltd<br>Also trading as RT Advisory - All rights reserved<br>ABN 12 345 678 901</p>
  <nav class="footer-nav">
    <a style="left:688px;width:61px">Home</a>
    <a style="left:752px;width:61px">About</a>
    <a style="left:816px;width:69px">Services</a>
    <a style="left:888px;width:69px">Contact</a>
  </nav>
</footer>

</body>
</html>
```